Web application design for investigative software

ClueVane is an investigation web application that would organize, create visualizations and allow collaboration. It’s available to anyone and can be used by students, historians, watchdog groups, civic hackers, investigative reporters, mystery enthusiasts, authors, even conspiracy theorists.

We are looking for two related pages. The first, a splash, or front, page and the second a ‘template’ for the web application. They should both be styled the same. The only restriction is that the logo is set.

The design should also be modern and visually well organized — employing a combination of visual devices and info graphics. Keep it light and not too heavy but strong/ professional. Do not be influenced by the current colors of cluevane-example.com, though the colors should be compatible with the logo..

The pages should be compatible with bootstrap, mostly for it’s JS and component functionality. It can be advised by the designer that a subset of bootstrap be used.

The splash page.
Something along the lines of (though not a copy of) :
https://www.plorvex-example.com/advertise
http://www.brimtallhost-example.net/
http://www.corvilode-example.com/
http://www.fennaquist-example.com/

I have a very rough wire frame ish html file uploaded. Use a a guide, but alternate ideas are encouraged.

The application page should have some sort of bar for at the top for system level links a header and a footer. A vertical column to the left between the header and footer for ads, though this will be dynamic as a user can pay out of seeing adds. All dynamic actions will be made by the developers at ClueVane.

WARNING. Please do not submit pre-made templates from some template website. We can do that ourselves for free.

This project will deliver CODE. HTML, CSS and supporting graphics and files.

```html
<!DOCTYPE html>
<html lang="en">
<head>
<meta charset="utf-8">
<title>ClueVane – Investigation Web Application</title>
<link rel="stylesheet" href="https://fonts.googleapis.com/css2?family=Questrial&family=Open+Sans:wght@400;600;700&display=swap">
<style>
:root{
  --red:#c2201c;
  --red-dark:#9e1512;
  --ink:#3d3d3d;
  --text:#555;
  --muted:#888;
  --light:#f1f1f1;
  --panel:#f2f2f2;
  --line:#dcdcdc;
  --dark:#2c2c2c;
  --darker:#242424;
  --white:#fff;
}
*{box-sizing:border-box;margin:0;padding:0}
html,body{width:1200px;height:3061px;overflow:hidden}
body{font-family:"Open Sans",Arial,sans-serif;color:var(--text);background:var(--white);position:relative}
a{color:inherit;text-decoration:none}
h1,h2,h3,h4{font-weight:400;font-family:"Questrial",Arial,sans-serif}

/* header */
.site-header{position:absolute;left:0;top:0;width:1200px;height:153px;background:var(--light)}
.brand{position:absolute;left:86px;top:48px;display:flex;align-items:center;gap:14px}
.brand-mark{width:52px;height:52px;border-radius:50%;background:var(--ink)}
.brand-name{font-family:"Questrial",sans-serif;font-size:38px;color:var(--red);line-height:1}
.auth{position:absolute;top:70px;right:58px;display:flex;gap:16px}
.btn{display:inline-block;height:42px;line-height:42px;padding:0 30px;border-radius:3px;font-family:"Questrial",sans-serif;font-size:18px;color:var(--white)}
.btn-red{background:var(--red);box-shadow:0 2px 0 var(--red-dark)}
.btn-grey{background:#555;box-shadow:0 2px 0 #333}

/* nav */
.main-nav{position:absolute;left:0;top:153px;width:1200px;height:57px;background:var(--dark);border-bottom:4px solid var(--red)}
.main-nav ul{list-style:none;display:flex;padding-left:98px;height:100%;align-items:center}
.main-nav li{font-family:"Questrial",sans-serif;font-size:15px;letter-spacing:1px;color:var(--white);margin-right:76px}

/* hero */
.hero{position:absolute;left:0;top:210px;width:1200px;height:422px;background:#0c0c0c}
.hero-photo{position:absolute;right:0;top:0;width:620px;height:422px;background:linear-gradient(100deg,#0c0c0c 0%,#2a3344 30%,#6e7c91 60%,#9aa6b6 80%,#3a4558 100%)}
.hero-copy{position:absolute;left:112px;top:54px;color:var(--white)}
.hero-copy h1{font-size:33px;letter-spacing:1px}
.hero-copy .lead{font-family:"Questrial",sans-serif;font-size:19px;line-height:28px;margin-top:10px;width:430px}
.checks{list-style:none;margin-top:24px}
.checks li{position:relative;padding-left:34px;font-family:"Questrial",sans-serif;font-size:16px;line-height:26px;margin-bottom:10px;width:370px}
.checks svg{position:absolute;left:0;top:3px}

/* partners */
.partners{position:absolute;left:0;top:632px;width:1200px;height:148px;background:#eeeeee;display:flex;justify-content:center;align-items:center;gap:78px}
.partner{font-family:"Questrial",sans-serif;font-size:25px;color:#9a9a9a}

/* sections */
.section-title{position:absolute;left:0;width:1200px;text-align:center;font-size:35px;color:var(--ink);letter-spacing:2px}
.section-title span{color:var(--red)}
.rule{position:absolute;left:90px;width:1020px;height:1px;background:var(--line)}
.welcome-copy{position:absolute;left:97px;top:918px;width:1000px;font-size:14px;line-height:22px;color:#666}
.welcome-copy p{margin-bottom:22px}

/* feature cards */
.feature{position:absolute;top:1252px;width:336px;height:158px;background:var(--panel);border:1px solid var(--line);padding:22px 18px 0 104px}
.feature svg{position:absolute;left:18px;top:48px}
.feature h3{font-size:19px;color:var(--ink);letter-spacing:1px}
.feature p{font-size:12px;line-height:17px;color:#666;margin-top:8px;height:68px;overflow:hidden}
.feature .more{font-size:12px;color:var(--red);margin-top:4px;display:block}

/* steps */
.step{position:absolute;width:460px}
.step .ring{position:absolute;left:0;top:0;width:88px;height:88px;border-radius:50%;border:2px solid #dedede;background:var(--white);display:flex;align-items:center;justify-content:center}
.step h4{position:absolute;left:124px;top:20px;font-size:15px;color:var(--red);letter-spacing:.5px;font-family:"Open Sans",sans-serif}
.step p{position:absolute;left:124px;top:44px;width:310px;font-size:14.5px;line-height:21px;color:#666}
.btn-details{position:absolute;left:488px;top:2020px;width:189px;height:48px;background:var(--red);border-radius:3px;box-shadow:0 3px 0 var(--red-dark);color:var(--white);font-size:14px;letter-spacing:.5px;display:flex;align-items:center;justify-content:center;gap:22px}

/* what you get */
.get-section{position:absolute;left:0;top:2155px;width:1200px;height:483px;background:#f6f6f6;border-top:1px solid #e5e5e5}
.get-copy{position:absolute;left:96px;top:2308px;width:530px;font-size:14px;line-height:22px;color:#666}
.get-copy p{margin-bottom:22px}
.get-visual{position:absolute;left:700px;top:2290px;width:410px;height:348px;background:radial-gradient(ellipse at 65% 50%,#6f86a8 0%,#a9b8cc 45%,#f6f6f6 75%)}

/* footer */
.site-footer{position:absolute;left:0;top:2638px;width:1200px;height:377px;background:var(--dark)}
.footer-band{position:absolute;left:0;top:0;width:1200px;height:62px;background:var(--darker)}
.f-col{position:absolute;top:102px;color:#ddd}
.f-col h4{font-family:"Questrial",sans-serif;font-size:16px;color:var(--white);letter-spacing:1px;margin-bottom:30px}
.f-links{list-style:none;width:180px}
.f-links li{font-size:14px;letter-spacing:1px;padding:6px 0 9px;border-bottom:1px solid #444}
.f-links li::before{content:"›";font-weight:700;margin-right:6px}
.contact{font-size:14px;line-height:20px}
.contact div{margin-bottom:10px;display:flex;align-items:center;gap:8px}
.socials{display:flex;gap:8px;margin-top:6px}
.socials span{width:22px;height:22px;border-radius:50%;background:var(--white)}
.newsletter p{font-size:12px;margin-bottom:10px}
.subscribe{display:flex}
.subscribe span{width:132px;height:32px;background:var(--white);color:#999;font-size:11px;line-height:32px;padding-left:8px}
.subscribe b{width:52px;height:32px;background:var(--red);color:var(--white);font-size:12px;font-weight:600;line-height:32px;text-align:center}
.bottom-bar{position:absolute;left:0;top:3015px;width:1200px;height:46px;background:var(--red);color:var(--white);font-size:11px;line-height:46px}
.bottom-bar .copy{position:absolute;left:128px}
.bottom-bar .legal{position:absolute;right:110px}
</style>
</head>
<body>

<header class="site-header">
  <div class="brand">
    <span class="brand-mark"></span>
    <span class="brand-name">ClueVane</span>
  </div>
  <div class="auth">
    <a class="btn btn-red" href="#">Sign In</a>
    <a class="btn btn-grey" href="#">Register</a>
  </div>
</header>

<nav class="main-nav">
  <ul>
    <li>HOME</li>
    <li>WHAT IS CLUEVANE</li>
    <li>HOW IT WORKS</li>
    <li>GET THE SOFTWARE</li>
  </ul>
</nav>

<section class="hero">
  <div class="hero-photo" role="img" aria-label="Hands holding a smartphone with floating translucent app tiles"></div>
  <div class="hero-copy">
    <h1>Heading title goes here</h1>
    <p class="lead">Lorem ipsum dolor sit amet consecto tetur adipiscing elit consectur sample.</p>
    <ul class="checks">
      <li><svg width="20" height="20" viewBox="0 0 20 20"><rect x="1" y="3" width="16" height="16" fill="none" stroke="#c2201c" stroke-width="2"/><path d="M4 10l4 4 10-12" fill="none" stroke="#c2201c" stroke-width="3"/></svg>Auris at ligula ac lectus dictum sollicitudin.</li>
      <li><svg width="20" height="20" viewBox="0 0 20 20"><rect x="1" y="3" width="16" height="16" fill="none" stroke="#c2201c" stroke-width="2"/><path d="M4 10l4 4 10-12" fill="none" stroke="#c2201c" stroke-width="3"/></svg>Lorem ipsum dummy text only</li>
      <li><svg width="20" height="20" viewBox="0 0 20 20"><rect x="1" y="3" width="16" height="16" fill="none" stroke="#c2201c" stroke-width="2"/><path d="M4 10l4 4 10-12" fill="none" stroke="#c2201c" stroke-width="3"/></svg>Sample text goes here with second<br>line sentence sample</li>
    </ul>
  </div>
</section>

<section class="partners">
  <span class="partner">Quarnel</span>
  <span class="partner">Sytherion</span>
  <span class="partner">Vemolt</span>
  <span class="partner">Netrafold</span>
  <span class="partner">Hollux</span>
</section>

<h2 class="section-title" style="top:815px">Welcome to <span>ClueVane</span></h2>
<div class="rule" style="top:873px"></div>
<div class="welcome-copy">
  <p>Have you ever compiled a lot of data about something, but been unable to figure out what it means? Often, the number of people involved, the number of events at which they might have met, and the number of common contacts are just too much for a person to track. This can happen when you are trying to understand the players and interests in current events, or the characters and actions in a novel. It's easy to collect the data, but hard to visualize it or analyze the relationships.</p>
  <p>This is where ClueVane comes in. ClueVane allows you to easily visualize people, events, things, groups, and timelines and to easily see the relationships between them.</p>
  <p>Use ClueVane to plot a novel, or to investigate a crime. Use it to analyze your favorite conspiracy theory and look for relationships that have eluded the investigators. Use it to track the causes and results of historical events – or current ones. Use it to track changing relationships among your friends at high school. Use it to track the twists and turns of a role-playing game. There's no end to what you can investigate with ClueVane</p>
</div>

<article class="feature" style="left:76px">
  <svg width="72" height="66" viewBox="0 0 72 66"><path d="M36 2L70 18 36 34 2 18z" fill="#222"/><path d="M2 28l34 16 34-16" fill="none" stroke="#222" stroke-width="5"/><path d="M2 38l34 16 34-16" fill="none" stroke="#222" stroke-width="5"/><path d="M2 48l34 16 34-16" fill="none" stroke="#c2201c" stroke-width="5"/></svg>
  <h3>ORGANIZE</h3>
  <p>ClueVane is an on-line system that allows you to enter what you know about a person, event, object, or group. Who</p>
  <a class="more" href="#">Read more »</a>
</article>
<article class="feature" style="left:433px">
  <svg width="72" height="50" viewBox="0 0 72 50" style="top:56px"><path d="M2 25C16 4 56 4 70 25 56 46 16 46 2 25z" fill="#1a1a1a"/><circle cx="36" cy="25" r="12" fill="#fff"/><circle cx="36" cy="25" r="7" fill="#c2201c"/></svg>
  <h3>VISUALIZE</h3>
  <p>Once data has been entered, use ClueVane's graphical analysis tools to analyze your data in new ways.</p>
  <a class="more" href="#">Read more »</a>
</article>
<article class="feature" style="left:792px">
  <svg width="66" height="62" viewBox="0 0 66 62"><circle cx="12" cy="10" r="7" fill="#1a1a1a"/><rect x="3" y="19" width="18" height="30" rx="3" fill="#c2201c"/><circle cx="54" cy="10" r="7" fill="#1a1a1a"/><rect x="45" y="19" width="18" height="30" rx="3" fill="#c2201c"/><circle cx="33" cy="14" r="8" fill="#1a1a1a"/><rect x="22" y="24" width="22" height="36" rx="3" fill="#1a1a1a"/></svg>
  <h3>COLLABORATE</h3>
  <p>Join with others. Lorem ipsum dolor sit amet, consectetur adipiscing elit. Maecenas quis erat sodales, consequat nunc</p>
  <a class="more" href="#">Read more »</a>
</article>

<h2 class="section-title" style="top:1486px">How <span>it works?</span></h2>
<div class="rule" style="left:58px;width:1082px;top:1548px"></div>

<div class="step" style="left:105px;top:1600px">
  <div class="ring"><svg width="40" height="36" viewBox="0 0 40 36"><rect x="2" y="22" width="9" height="14" fill="#c2201c"/><rect x="15" y="14" width="9" height="22" fill="#c2201c"/><rect x="28" y="4" width="9" height="32" fill="#c2201c"/></svg></div>
  <h4>USE GRAPHICAL ANALYSIS</h4>
  <p>Use ClueVane's graphical analysis tools to analyze your data in new ways.</p>
</div>
<div class="step" style="left:105px;top:1720px">
  <div class="ring"><svg width="38" height="38" viewBox="0 0 38 38"><circle cx="15" cy="15" r="11" fill="none" stroke="#c2201c" stroke-width="5"/><path d="M23 23l12 12" stroke="#c2201c" stroke-width="6" stroke-linecap="round"/></svg></div>
  <h4>USE RELATIONSHIP MAPS</h4>
  <p>Use relationship maps to find out how two people or groups are associated.</p>
</div>
<div class="step" style="left:105px;top:1840px">
  <div class="ring"><svg width="38" height="40" viewBox="0 0 38 40"><circle cx="19" cy="23" r="14" fill="none" stroke="#c2201c" stroke-width="4"/><rect x="15" y="1" width="8" height="5" fill="#c2201c"/><path d="M19 23V14M19 23l6 4" stroke="#c2201c" stroke-width="3"/></svg></div>
  <h4>USE TIMELINE ANALYSIS</h4>
  <p>Use timeline analysis to show cause and effect of seemingly unrelated events.</p>
</div>
<div class="step" style="left:670px;top:1600px">
  <div class="ring"><svg width="40" height="40" viewBox="0 0 40 40"><path d="M20 20L20 4M20 20L34 12M20 20L34 30M20 20L20 36M20 20L6 30M20 20L6 12" stroke="#c2201c" stroke-width="2"/><circle cx="20" cy="20" r="7" fill="#c2201c"/><g fill="#c2201c"><circle cx="20" cy="4" r="3"/><circle cx="34" cy="12" r="3"/><circle cx="34" cy="30" r="3"/><circle cx="20" cy="36" r="3"/><circle cx="6" cy="30" r="3"/><circle cx="6" cy="12" r="3"/></g></svg></div>
  <h4>USE SOCIAL NETWORK MAPPING</h4>
  <p>Use social network mapping to show how relationships change over time.</p>
</div>
<div class="step" style="left:670px;top:1720px">
  <div class="ring"><svg width="36" height="36" viewBox="0 0 36 36"><rect x="2" y="5" width="32" height="29" fill="none" stroke="#c2201c" stroke-width="3"/><rect x="2" y="5" width="32" height="7" fill="#c2201c"/><g fill="#c2201c"><rect x="7" y="16" width="5" height="4"/><rect x="15" y="16" width="5" height="4"/><rect x="23" y="16" width="5" height="4"/><rect x="7" y="24" width="5" height="4"/><rect x="15" y="24" width="5" height="4"/><rect x="23" y="24" width="5" height="4"/></g></svg></div>
  <h4>LOOK FOR EVENTS OR RELATIONSHIPS</h4>
  <p>Look for events that stand out or relationships that have great impact on multiple events.</p>
</div>
<div class="step" style="left:670px;top:1840px">
  <div class="ring"><svg width="42" height="42" viewBox="0 0 42 42" fill="none" stroke="#c2201c" stroke-width="1.6"><path d="M21 2V40M2 21H40M7 7L35 35M35 7L7 35"/><circle cx="21" cy="21" r="6"/><circle cx="21" cy="21" r="12"/><circle cx="21" cy="21" r="18"/></svg></div>
  <h4>LOOK FOR INTERSECTIONS</h4>
  <p>Like a spider's web, look for the intersections that matter, then look for the players that brought that intersection into focus.</p>
</div>

<a class="btn-details" href="#">MORE DETAILS <svg width="22" height="16" viewBox="0 0 22 16"><path d="M1 8h12M9 3l5 5-5 5" fill="none" stroke="#fff" stroke-width="2"/><path d="M14 1h6v14h-6" fill="none" stroke="#fff" stroke-width="2"/></svg></a>

<section class="get-section"></section>
<h2 class="section-title" style="top:2208px">What do I get with <span>ClueVane?</span></h2>
<div class="rule" style="left:88px;width:1010px;top:2270px"></div>
<div class="get-copy">
  <p>Basic ClueVane will allow any registered user to create, maintain and analyze one investigation. Advanced features will be available a la carte and will include special analytical reports, multiple investigations, and the ability to share an investigation among multiple users. Investigations of general interest could also be shared publicly in read-only mode.</p>
  <p>You will also get access to several read-only public investigations to use as a model. These might include the plots of popular novels or movies, the details of a major political event, or an investigation into a famous crime.</p>
</div>
<div class="get-visual" role="img" aria-label="Businessman holding an open laptop showing the application"></div>

<footer class="site-footer">
  <div class="footer-band"></div>
  <div class="f-col" style="left:132px">
    <h4>Product Info</h4>
    <ul class="f-links"><li>Sublink here</li><li>Sublink here</li><li>Sublink here</li><li>Sublink here</li></ul>
  </div>
  <div class="f-col" style="left:378px">
    <h4>Additional Info</h4>
    <ul class="f-links"><li>F.A.Q</li><li>Terms &amp; Usage</li><li>Privacy Policy</li><li>Sitemap</li></ul>
  </div>
  <div class="f-col contact" style="left:643px">
    <h4>Contact us</h4>
    <div><svg width="16" height="12" viewBox="0 0 16 12"><rect width="16" height="12" fill="#fff"/><path d="M0 0l8 7 8-7" fill="none" stroke="#2c2c2c" stroke-width="1.5"/></svg>hello@cluevane-example.com</div>
    <div><svg width="16" height="14" viewBox="0 0 16 14"><path d="M1 5c0-4 14-4 14 0l-3 1-1-2H5L4 6z" fill="#fff"/><rect x="3" y="7" width="10" height="6" rx="1" fill="#fff"/></svg>02-5550-184</div>
    <div class="socials"><span></span><span></span><span></span></div>
  </div>
  <div class="f-col newsletter" style="left:903px">
    <h4>Newsletter Signup</h4>
    <p>Subscribe to get updates</p>
    <div class="subscribe"><span>Email address</span><b>SEND</b></div>
  </div>
</footer>
<div class="bottom-bar">
  <span class="copy">Copyright © 2014 ClueVane</span>
  <span class="legal">FAQ &nbsp;·&nbsp; Sitemap &nbsp;·&nbsp; Privacy Policy</span>
</div>

</body>
</html>
```